Townhome Multi-Family Property Exterior Sign

Hello. We are looking for a new design for our exterior pylon for for a multi-family housing property in Texas. The design will need to go on a new sign panel to replace the existing (see photo of existing). We are looking to see both modern and contemporary designs. Included the sign should be the name, Loma Brisa Townhomes and the web address www.lomabrisatownhomes.example.

Attached here is a PDF file of the proposed new sign shape. We are open to other shape ideas as well if your design would better suit a more rectangular shape.

Industry/Entity Type

Property

Font styles to use
Serif
Sans Serif

Colors
9bcb3c

Requirements
Must have
• Name of building: Loma Brisa Townhomes
• Website: www.lomabrisatownhomes.example
Nice to have
• Address: 420-530 Halvorsen Lane (only if it fits nicely)

```html
<!DOCTYPE html>
<html lang="en">
<head>
<meta charset="utf-8">
<title>Loma Brisa Townhomes – Exterior Sign Panel</title>
<link rel="stylesheet" href="https://fonts.googleapis.com/css2?family=Montserrat:wght@700;800&display=swap">
<style>
  :root {
    --backdrop: #1f1f21;
    --panel-light: #f4f8fb;
    --panel-tint: #d9eaf6;
    --brand-green: #2bae4a;
    --brand-green-deep: #0f9447;
    --title-green: #2aad4b;
    --title-dark: #323437;
    --on-green: #ffffff;
  }
  html, body {
    margin: 0;
    padding: 0;
    width: 1200px;
    height: 1000px;
    overflow: hidden;
    background: var(--backdrop);
  }
  .canvas {
    position: relative;
    width: 1200px;
    height: 1000px;
  }
  .sign-panel {
    position: absolute;
    left: 84px;
    top: 305px;
    width: 1030px;
    height: 418px;
    display: block;
  }
  .sign-title {
    font-family: "Montserrat", sans-serif;
    font-weight: 800;
  }
  .sign-title--name { fill: var(--title-green); }
  .sign-title--type { fill: var(--title-dark); }
  .sign-web {
    font-family: "Montserrat", sans-serif;
    font-weight: 800;
    font-size: 33px;
    fill: var(--on-green);
  }
  .sign-address {
    font-family: "Montserrat", sans-serif;
    font-weight: 700;
    font-size: 25px;
    fill: var(--on-green);
  }
  .web-icon { stroke: var(--on-green); fill: none; stroke-width: 2.2; }
</style>
</head>
<body>
<main class="canvas">
  <svg class="sign-panel" viewBox="0 0 1030 418" xmlns="http://www.w3.org/2000/svg" aria-label="Loma Brisa Townhomes sign panel">
    <defs>
      <linearGradient id="panelFace" x1="0" y1="0" x2="1" y2="1">
        <stop offset="0" stop-color="var(--panel-tint)"/>
        <stop offset="0.45" stop-color="var(--panel-light)"/>
        <stop offset="1" stop-color="var(--panel-tint)"/>
      </linearGradient>
      <linearGradient id="greenBand" x1="0" y1="0" x2="1" y2="0">
        <stop offset="0" stop-color="var(--brand-green)"/>
        <stop offset="1" stop-color="var(--brand-green-deep)"/>
      </linearGradient>
    </defs>

    <rect class="panel-face" x="0" y="0" width="1030" height="418" fill="url(#panelFace)"/>
    <path class="panel-band" d="M0 327 Q515 229 1030 327 L1030 418 L0 418 Z" fill="url(#greenBand)"/>

    <text class="sign-title sign-title--name" x="81" y="143" font-size="118" textLength="845" lengthAdjust="spacingAndGlyphs">LOMA BRISA</text>
    <text class="sign-title sign-title--type" x="76" y="250" font-size="128" textLength="855" lengthAdjust="spacingAndGlyphs">TOWNHOMES</text>

    <g class="web-icon" transform="translate(139 338)">
      <circle r="14"/>
      <ellipse rx="6" ry="14"/>
      <line x1="-14" y1="0" x2="14" y2="0"/>
      <path d="M-12 -7 H12 M-12 7 H12"/>
    </g>
    <text class="sign-web" x="167" y="350">WWW.LOMABRISATOWNHOMES.EXAMPLE</text>
    <text class="sign-address" x="516" y="392" text-anchor="middle">420-530 HALVORSEN LANE</text>
  </svg>
</main>
</body>
</html>
```